Dovenmarch Luxury Landscapes

A landscape business card.

Target Market(s)

Middle aged and up. Professionals.

Industry/Entity Type

Landscape

Contact Information for Business Card

Thornbeck

Colors
0054AA
0677BA
7BADD7
CADEEF
E8F1F8
0094D4
00A9DD
6FCCEA
C7EBF8
E9F6FB

Requirements
Must have
• The color blue and silver be very attractive
Nice to have
• An embossed logo. A watermark of a plant or something that indicates that we are a landscape company in the background of the backside where list of services are offered. . List of services on the back.
Should not have
• Red, yellow, orange.

```html
<!DOCTYPE html>
<html lang="en">
<head>
<meta charset="utf-8">
<title>Dovenmarch Luxury Landscapes – Business Card</title>
<link rel="stylesheet" href="https://fonts.googleapis.com/css2?family=Marcellus&family=Poppins:wght@400&display=swap">
<style>
  :root {
    --stage: #2a2b2e;
    --card-white: #ffffff;
    --card-black: #17181a;
    --brand-blue: #2b3ea6;
    --silver: #b9bcc2;
    --silver-light: #d6d9de;
    --ink: #1b1b1b;
    --gloss-deep: #0c0d0e;
    --gloss-mid: #1c1d20;
    --gloss-sheen: #55585e;
  }
  * { margin: 0; padding: 0; box-sizing: border-box; }
  html, body {
    width: 1200px; height: 1108px; overflow: hidden;
    background: var(--stage);
  }
  .stage {
    position: relative; width: 1200px; height: 1108px;
    display: flex; justify-content: center; align-items: center; gap: 80px;
  }
  .card {
    width: 420px; height: 735px; border-radius: 26px;
    position: relative; overflow: hidden;
  }
  .card-front {
    background: var(--card-white);
    display: flex; flex-direction: column; align-items: center;
    padding-top: 100px; text-align: center;
  }
  .brand-dot {
    width: 140px; height: 140px; border-radius: 50%;
    border: 6px solid var(--silver);
    margin-bottom: 44px;
  }
  .brand-name {
    font-family: "Marcellus", serif; color: var(--brand-blue);
    font-size: 52px; line-height: 1; letter-spacing: 2px;
  }
  .brand-tagline {
    font-family: "Marcellus", serif; color: var(--brand-blue);
    font-size: 21px; letter-spacing: 3px; margin-top: 12px;
  }
  .person-name {
    font-family: "Marcellus", serif; color: var(--brand-blue);
    font-size: 30px; letter-spacing: 0.5px; margin-top: 70px;
  }
  .rule {
    width: 110px; height: 2px; background: var(--brand-blue);
    margin: 16px auto;
  }
  .contact {
    font-family: "Poppins", sans-serif; color: var(--ink);
    font-size: 19px; line-height: 1.45;
  }
  .contact .web-accent { color: var(--brand-blue); }
  .card-back { background: var(--card-black); }
  .back-pattern {
    position: absolute; inset: 0;
    background:
      radial-gradient(circle at 95% 10%, rgba(150,154,162,0.45) 0%, rgba(150,154,162,0) 45%),
      linear-gradient(215deg, var(--gloss-sheen) 0%, var(--gloss-mid) 45%, var(--gloss-deep) 100%);
  }
  .back-mark {
    position: absolute; left: 200px; top: 500px;
    display: flex; align-items: center; gap: 10px;
  }
  .back-mark-dot {
    width: 14px; height: 14px; border-radius: 50%;
    background: var(--brand-blue);
    border: 2px solid var(--silver);
  }
  .back-mark-name {
    font-family: "Marcellus", serif; color: var(--silver-light);
    font-size: 28px; letter-spacing: 1px;
  }
</style>
</head>
<body>
<main class="stage">
  <section class="card card-front">
    <div class="brand-dot"></div>
    <h1 class="brand-name">DOVENMARCH</h1>
    <p class="brand-tagline">LUXURY LANDSCAPES</p>
    <h2 class="person-name">MARA KETTLEBY</h2>
    <div class="rule"></div>
    <p class="contact">902-555-0183<br>www.<span class="web-accent">Dovenmarch</span>.com</p>
    <div class="rule"></div>
    <p class="contact">41B Hollis Lane, Thornbeck<br>Nova Scotia, B3K 4P2.</p>
  </section>
  <section class="card card-back">
    <div class="back-pattern" role="img" aria-label="Tonal gloss pattern of repeated monogram marks on black, brighter toward the top right"></div>
    <div class="back-mark">
      <span class="back-mark-dot"></span>
      <span class="back-mark-name">Dovenmarch</span>
    </div>
  </section>
</main>
</body>
</html>
```